Pamphlet for introducing people to our church

I would like a church pamphlet designed, that includes the content in file "tovik-pamphlet.txt".

I am looking for a design that will incorporate the content in a professional and creative manner.

You do not have to use the content in any specific order, but I am relying on your skill and design knowledge to organize everything in an artistic and effective way.

Target Market(s)

Everyone

Industry/Entity Type

Religious

Requirements
Must have
• logo, use of content provided, use of branding (logo colors)
Nice to have
• More images where necessary
Should not have
• cross

```html
<!DOCTYPE html>
<html lang="en">
<head>
<meta charset="utf-8">
<title>Tovik — Church Pamphlet</title>
<link href="https://fonts.googleapis.com/css2?family=Cinzel:wght@400;600&family=Montserrat:wght@500;600&family=PT+Sans:wght@400&display=swap" rel="stylesheet">
<style>
  :root{
    --bg:#5c5c5c;
    --navy:#0d3461;
    --gold:#e69a2a;
    --white:#ffffff;
    --photo-warm-1:#f3c27a;
    --photo-warm-2:#b8612a;
    --photo-warm-3:#6b3218;
    --glass-1:#f7d24a;
    --glass-2:#c2521a;
    --glass-3:#4a1e10;
  }
  *{margin:0;padding:0;box-sizing:border-box}
  html,body{width:1200px;height:960px;overflow:hidden;background:var(--bg)}
  .canvas{position:relative;width:1200px;height:960px;background:var(--bg)}
  .page{position:absolute;top:200px;width:415px;height:588px;background:var(--navy);overflow:hidden;box-shadow:0 6px 18px rgba(0,0,0,.35)}
  .page--front{left:152px}
  .page--back{left:673px}
  .page svg{position:absolute;inset:0;display:block}
  .heading{font-family:"Cinzel",serif;font-weight:600;color:var(--gold);letter-spacing:.5px}
  .body-copy{font-family:"PT Sans",sans-serif;color:var(--white);font-size:10.5px;line-height:1.22}

  /* front */
  .brand{position:absolute;left:28px;top:226px}
  .brand__name{display:flex;align-items:center;gap:10px;font-family:"Cinzel",serif;font-weight:400;font-size:46px;color:var(--white);line-height:1}
  .brand__dot{width:14px;height:14px;border-radius:50%;background:var(--gold)}
  .front-content{position:absolute;left:28px;right:42px;top:302px}
  .front-content .heading{font-size:15px;margin-bottom:2px}
  .front-content .section{margin-bottom:10px}
  .front-url{font-family:"Cinzel",serif;font-weight:600;color:var(--gold);font-size:14px;margin-top:10px}

  /* back */
  .contact{position:absolute;left:31px;top:34px;width:260px}
  .contact__label{font-family:"Cinzel",serif;font-weight:600;color:var(--gold);font-size:14.5px;line-height:1.18}
  .contact__value{font-family:"Montserrat",sans-serif;font-weight:500;color:var(--white);font-size:13px;line-height:1.35;text-transform:uppercase}
  .contact__value--strong{font-weight:600;font-size:14.5px}
  .contact__group{margin-bottom:13px}
</style>
</head>
<body>
<div class="canvas">

  <section class="page page--front">
    <svg width="415" height="588" viewBox="0 0 415 588">
      <defs>
        <radialGradient id="warm-light" cx="0.25" cy="0.1" r="1">
          <stop offset="0" stop-color="var(--photo-warm-1)"/>
          <stop offset="0.55" stop-color="var(--photo-warm-2)"/>
          <stop offset="1" stop-color="var(--photo-warm-3)"/>
        </radialGradient>
      </defs>
      <rect role="img" aria-label="Photo of a young girl looking up into warm autumn sunlight" x="0" y="0" width="415" height="270" fill="url(#warm-light)"/>
      <path d="M0 165 C40 140 150 125 192 160 C205 200 210 250 250 258 C295 266 320 222 350 220 C380 218 402 222 415 228 L415 588 L0 588 Z" fill="var(--navy)"/>
      <path d="M192 160 C205 200 210 250 250 258 C295 266 320 222 350 220" fill="none" stroke="var(--gold)" stroke-width="3"/>
    </svg>
    <div class="brand">
      <div class="brand__name"><span class="brand__dot"></span>TOVIK</div>
    </div>
    <div class="front-content">
      <div class="section">
        <h2 class="heading">MISSION STATEMENT</h2>
        <p class="body-copy">TOVIK is a gathering of believers whose purpose is to seek the face of God for an authentic restoration of the church as a body of born again believers around the world. As a gathering of believers, TOVIK seeks an awakening of the mind founded on the precepts and teachings of Jesus Christ. The modern church has replaced the simple and Kingdom centered principles of Jesus's disciples with complacent and compromised teachings on earthly prosperity. We believe in humbly seeking God without motive to use God or His Word for our own gain. The end times church will experience a glorious revival, renewed love and zeal for true discipleship, faith, and godliness as Jesus intended for us.</p>
      </div>
      <div class="section">
        <h2 class="heading">MINISTRIES</h2>
        <p class="body-copy">Kingdom seeds (Children's ministry) Children learn to be seeds of godliness in the world. School of pilgrims Learn the basics of Christian faith and about God's purpose for your life. School of disciples Deepen your knowledge of God's word and learn how to serve Him.</p>
      </div>
      <div class="front-url">WWW.TOVIK.ORG</div>
    </div>
  </section>

  <section class="page page--back">
    <svg width="415" height="588" viewBox="0 0 415 588">
      <defs>
        <linearGradient id="glass-light" x1="0" y1="0" x2="0.3" y2="1">
          <stop offset="0" stop-color="var(--photo-warm-2)"/>
          <stop offset="0.45" stop-color="var(--glass-3)"/>
          <stop offset="0.75" stop-color="var(--glass-2)"/>
          <stop offset="1" stop-color="var(--glass-1)"/>
        </linearGradient>
      </defs>
      <path role="img" aria-label="Photo of a cathedral interior with a glowing stained glass window" d="M275 0 C252 50 290 95 308 140 C325 185 290 230 275 250 C258 275 275 300 310 300 C335 300 325 335 290 355 C230 385 170 400 155 465 C145 515 160 560 175 588 L415 588 L415 0 Z" fill="url(#glass-light)"/>
    </svg>
    <div class="contact">
      <div class="contact__group">
        <div class="contact__label">SUNDAY SERVICE:</div>
        <div class="contact__value">10:00AM–12:30PM</div>
      </div>
      <div class="contact__group">
        <div class="contact__value">Alder Community Hall<br>48 Harbor Lane<br>Westbrook, ME 04092</div>
      </div>
      <div class="contact__group">
        <div class="contact__label">VISIT US AT</div>
        <div class="contact__value">www.tovik.org</div>
      </div>
      <div class="contact__group">
        <div class="contact__label">IF YOU NEED PRAYER<br>OR COUNSELING<br>GIVE US A CALL AT</div>
        <div class="contact__value contact__value--strong">+1 555-014-2288</div>
      </div>
      <div class="contact__group">
        <div class="contact__label">OR EMAIL US AT</div>
        <div class="contact__value">contact@<br>cedarmeadow.org</div>
      </div>
    </div>
  </section>

</div>
</body>
</html>
```